Vellora Labs - Mushroom Supplement Packaging

Our brand is called Vellora Labs. I've added a couple different logos that you can use. We are creating a line up of Mushroom Supplement products. I will add the entire line-up of products here. I've added examples of other products and packaging shape types I can purchase. Give me different options for packaging that is minimalist and clean for this brand that makes it look really well made and clean and make people want to buy.

Product 1 Lions Mane 1g
Product 2 Cordyceps 1g
Product 3 Chaga 1g
Product 4 Turkey Tail 1g
Product 5 Reishi 1g
Product 6 Maitake 1g
Product 7 Shiitake 1g

Product 8 (Mix) Lions Mane 143mg
Cordyceps 143mg
Chaga 143mg
Turkey Tail 143mg
Reishi 143mg
Maitake 143mg
Shiitake 143mg

```html
<!DOCTYPE html>
<html lang="en">
<head>
<meta charset="utf-8">
<title>Lion's Mane Mushroom – Label</title>
<link href="https://fonts.googleapis.com/css2?family=Montserrat:wght@400;500&display=swap" rel="stylesheet">
<style>
  :root {
    --label-navy: #0d141c;
    --label-navy-light: #1a222c;
    --text-white: #f2f2f2;
    --text-muted: #c9ccd1;
    --accent-tan: #e2c19c;
    --accent-gold: #c8a47c;
    --band-text: #5a4a3a;
    --illustration-light: #e9e9e9;
    --illustration-shade: #bfc2c6;
  }
  * { margin: 0; padding: 0; box-sizing: border-box; }
  html, body { width: 1200px; height: 800px; overflow: hidden; }
  body {
    font-family: "Montserrat", sans-serif;
    background: linear-gradient(90deg, var(--label-navy-light) 0%, var(--label-navy) 45%, var(--label-navy) 100%);
    position: relative;
  }
  .label { position: absolute; inset: 0; }

  .claims {
    position: absolute; left: 346px; top: 44px;
    font-size: 13px; line-height: 23px; letter-spacing: 0.02em;
    color: var(--text-muted); text-transform: uppercase;
  }

  .product-title {
    position: absolute; left: 0; right: 0; top: 112px;
    text-align: center; color: var(--text-white);
    font-weight: 400; font-size: 80px; line-height: 96px;
    letter-spacing: 0.01em; text-transform: uppercase;
  }

  .mushroom-art {
    position: absolute; left: 447px; top: 303px;
    width: 307px; height: 276px;
    border-radius: 48% 52% 46% 50% / 46% 50% 54% 52%;
    background: radial-gradient(ellipse at 55% 35%, var(--illustration-light) 0%, var(--illustration-shade) 100%);
  }

  .dose {
    position: absolute; left: 714px; top: 536px;
    font-size: 15px; line-height: 30px; font-weight: 500;
    letter-spacing: 0.08em; color: var(--text-white); text-transform: uppercase;
  }

  .supplement-band {
    position: absolute; left: 298px; top: 489px;
    width: 100px; height: 311px;
    background: var(--accent-tan);
    display: flex; justify-content: center; padding-top: 18px;
  }
  .supplement-band__text {
    writing-mode: vertical-rl; text-transform: uppercase;
    color: var(--band-text);
  }
  .supplement-band__main {
    display: block; font-size: 32px; line-height: 40px;
    letter-spacing: 0.2em; font-weight: 500;
  }
  .supplement-band__sub {
    display: block; font-size: 19px; line-height: 26px;
    letter-spacing: 0.2em; font-weight: 500;
  }

  .features {
    position: absolute; left: 443px; top: 608px; list-style: none;
  }
  .feature {
    display: flex; align-items: center; height: 58px;
    color: var(--accent-gold); font-size: 37px; letter-spacing: 0.36em;
    text-transform: uppercase;
  }
  .feature__icon { width: 40px; height: 40px; margin-right: 33px; flex: none; }
</style>
</head>
<body>
  <main class="label">
    <div class="claims">
      <p>Supports a healthy immune system</p>
      <p>Supports overall well-being</p>
    </div>

    <h1 class="product-title">Lion's Mane<br>Mushroom</h1>

    <div class="mushroom-art" role="img" aria-label="White line illustration of a shaggy lion's mane mushroom"></div>

    <div class="dose">
      <p>120 Capsules</p>
      <p>1000 mg in each</p>
    </div>

    <div class="supplement-band">
      <p class="supplement-band__text">
        <span class="supplement-band__main">Dietary</span>
        <span class="supplement-band__sub">Supplement</span>
      </p>
    </div>

    <ul class="features">
      <li class="feature">
        <svg class="feature__icon" viewBox="0 0 40 40" aria-hidden="true">
          <circle cx="14" cy="24" r="9" fill="var(--accent-gold)"/>
          <circle cx="26" cy="24" r="9" fill="var(--accent-gold)"/>
          <circle cx="20" cy="12" r="6" fill="var(--accent-gold)"/>
        </svg>
        Organic
      </li>
      <li class="feature">
        <svg class="feature__icon" viewBox="0 0 40 40" aria-hidden="true">
          <path d="M4 22 C10 12 20 14 20 26 C12 28 6 26 4 22 Z" fill="var(--accent-gold)"/>
          <path d="M20 26 C20 14 30 10 38 12 C36 24 28 28 20 26 Z" fill="var(--accent-gold)"/>
        </svg>
        Natural
      </li>
      <li class="feature">
        <svg class="feature__icon" viewBox="0 0 40 40" aria-hidden="true">
          <path d="M8 4 C22 14 4 26 18 36 M18 4 C4 14 22 26 8 36" stroke="var(--accent-gold)" stroke-width="3" fill="none"/>
          <circle cx="31" cy="20" r="6" stroke="var(--accent-gold)" stroke-width="2.5" fill="none"/>
          <line x1="27" y1="24" x2="35" y2="16" stroke="var(--accent-gold)" stroke-width="2.5"/>
        </svg>
        Gluten Free
      </li>
    </ul>
  </main>
</body>
</html>
```